Business Card Design for Cybersecurity Company - Quorvent Systems

We need a business card design for our new cybersecurity company, Quorvent. We’re going for a clean, hi tech look that feels modern, premium, and trustworthy. We want a design that really stands out and makes people say WOW when we hand it over!

Quorvent delivers reliable IT support and managed services for small and mid sized businesses. We help companies stay secure, efficient, and connected through proactive monitoring, cybersecurity services, cloud management, and remote support.

Target Market(s)

Designers should target small and mid sized businesses that need dependable cybersecurity and IT support.

Industry/Entity Type

Cybersecurity, Managed Service Provider, IT services

Contact Information for Business Card

Contact information

Requirements
Must have
• The card should look clean, modern, and tech focused, with the Quorvent logo, clear contact info, and strong readability. It needs to feel premium and professional while still keeping a simple layout that fits a cybersecurity and IT brand.
Nice to have
• Nice to have elements include subtle touches that give the card a modern, tech feel, along with a layout that works well in different background styles.
Should not have
• The card should avoid clutter, loud graphics, or anything that takes attention away from the logo and contact details.

```html
<!DOCTYPE html>
<html lang="en">
<head>
<meta charset="utf-8">
<title>Quorvent Systems – Business Card</title>
<link rel="stylesheet" href="https://fonts.googleapis.com/css2?family=Roboto:wght@400;500;700&display=swap">
<style>
  :root {
    --page-bg: #eceef1;
    --card-white: #ffffff;
    --ink: #222230;
    --ink-soft: #2e2e38;
    --accent-purple: #6a3fa0;
    --accent-blue: #4673bb;
    --back-start: #4874bd;
    --back-end: #614ca2;
    --pattern-tone: #eef0f5;
  }
  * { margin: 0; padding: 0; box-sizing: border-box; }
  html, body {
    width: 1200px; height: 1200px; overflow: hidden;
    background: var(--page-bg);
    font-family: "Roboto", Arial, sans-serif;
  }
  .canvas { position: relative; width: 1200px; height: 1200px; }

  .card { position: absolute; left: 150px; width: 900px; height: 527px; overflow: hidden; }
  .card--front { top: 54px; background: var(--card-white); }
  .card--back {
    top: 619px;
    background: linear-gradient(35deg, var(--back-start) 0%, var(--back-end) 100%);
  }

  .circuit-texture {
    position: absolute; left: 0; top: 0; width: 450px; height: 252px;
    background: radial-gradient(ellipse at 30% 40%, var(--pattern-tone) 0%, rgba(238,240,245,0.5) 45%, rgba(255,255,255,0) 75%);
  }

  .brand {
    position: absolute; display: flex; align-items: center; gap: 14px;
    font-weight: 500; white-space: nowrap;
  }
  .brand__mark { display: block; }
  .brand--front { right: 70px; top: 108px; color: var(--ink); font-size: 38px; }
  .brand--front .brand__mark { width: 30px; height: 30px; background: var(--accent-purple); }
  .brand--back { left: 50%; top: 50%; transform: translate(-50%, -50%); color: #ffffff; font-size: 66px; gap: 24px; }
  .brand--back .brand__mark { width: 52px; height: 52px; background: #ffffff; }

  .person { position: absolute; left: 62px; top: 258px; }
  .person__name {
    font-size: 38px; font-weight: 700; color: var(--accent-purple); letter-spacing: 0.3px; line-height: 1;
  }
  .person__role { margin-top: 20px; font-size: 22px; color: var(--ink-soft); }

  .divider {
    position: absolute; left: 62px; top: 373px; width: 419px; height: 2px;
    background: linear-gradient(90deg, var(--accent-purple), var(--accent-blue));
  }

  .contacts {
    position: absolute; left: 62px; top: 396px;
    display: grid; grid-template-columns: 248px auto; row-gap: 17px;
    font-size: 23px; color: var(--ink-soft);
  }
  .contact { display: flex; align-items: center; gap: 13px; line-height: 24px; }
  .contact__icon { width: 14px; height: 14px; fill: var(--accent-purple); flex: none; }
</style>
</head>
<body>
<main class="canvas">
  <section class="card card--front" aria-label="Card front">
    <div class="circuit-texture" role="img" aria-label="Faint circuit-line pattern"></div>

    <div class="brand brand--front">
      <span class="brand__mark"></span>
      <span class="brand__name">Quorvent Systems</span>
    </div>

    <div class="person">
      <h1 class="person__name">DANA HOLLIS</h1>
      <p class="person__role">Owner | CEO | Quorvent Systems</p>
    </div>

    <div class="divider"></div>

    <ul class="contacts" style="list-style:none">
      <li class="contact">
        <svg class="contact__icon" viewBox="0 0 16 16" aria-hidden="true"><path d="M3.3 1.2l2.3 2.7-1.3 1.8c.9 2 2.5 3.6 4.5 4.6l1.8-1.3 2.7 2.3-1 2.5C6.8 13.4 2.6 9.2 1 3.5z"/></svg>
        <span>(855) 310-QVNT</span>
      </li>
      <li class="contact">
        <svg class="contact__icon" viewBox="0 0 16 16" aria-hidden="true"><path d="M6 .5h6a1 1 0 0 1 1 1v13a1 1 0 0 1-1 1H6a1 1 0 0 1-1-1v-13a1 1 0 0 1 1-1zm.5 2v10h5v-10z"/></svg>
        <span>dana@quorvent.com</span>
      </li>
      <li class="contact">
        <svg class="contact__icon" viewBox="0 0 16 16" aria-hidden="true"><path d="M4 .5h8a1 1 0 0 1 1 1v13a1 1 0 0 1-1 1H4a1 1 0 0 1-1-1v-13a1 1 0 0 1 1-1zm.8 2v10h6.4v-10z"/></svg>
        <span>(813) 555-0142</span>
      </li>
      <li class="contact">
        <svg class="contact__icon" viewBox="0 0 16 16" aria-hidden="true"><path d="M8 1a7 7 0 1 0 0 14A7 7 0 0 0 8 1zm0 1.6c.8 0 1.6 1.5 1.9 3.6H6.1C6.4 4.1 7.2 2.6 8 2.6zM2.7 7.4h2.2v1.2H2.7zm3.4 0h3.8v1.2H6.1zm5 0h2.2v1.2h-2.2zM6.1 9.8h3.8c-.3 2.1-1.1 3.6-1.9 3.6s-1.6-1.5-1.9-3.6z"/></svg>
        <span>quorvent.com</span>
      </li>
    </ul>
  </section>

  <section class="card card--back" aria-label="Card back">
    <div class="brand brand--back">
      <span class="brand__mark"></span>
      <span class="brand__name">Quorvent Systems</span>
    </div>
  </section>
</main>
</body>
</html>
```